Postcard Design

I need a two-sided promotional postcard designed to address the key business areas of my gluten free wellness retreat.

Please Note: The "mailer" template is not required for the reverse as these postcards are for event handouts only. Please use the attached "front" template for each side (both front and back)

Possibly, services on one side and photos/visuals on the other side with contact information on either or both sides.

www.hollowpinekitchen.net is my website.

Key business areas:

STAY: Retreat stays + associated care program
PLAY: Bed and Breakfast
LEARN: Individual Health Coaching
GROW: Community classes / events / cooking classes

Retreat Stay Client: Female, 40+. Expendable income, but she likely has a very busy career and family so she does not have the time to spend this on herself. Her wellness takes a backseat to her career and family life. She often remembers being “thinner when she was younger” and has a lot of preconceived notions about dieting. She is open to alternative healthcare options, and thinks she does a pretty good job keeping up with them via Dr. Vel, and magazine articles etc. She needs a compassionate, non-intimidating care provider who she trusts will not “judge” her.

Coaching Client: Male + Female, from mid-40s to retirement age and older. They likely also have some amount of expendable income, and are not necessarily bound my medical or other insurance in terms of seeking alternative treatment. In their earlier adult years they were likely active and well-traveled. They have some adult children who are also quite successful, and so in their golden years, they are comfortable to spend money on themselves rather than assist adult children/grandkids. Frankly, they can somewhat skeptical of alternative wellness providers. They likely suffer from a myriad of age related maladies, and need a compassionate standard of care.

Visual Identity:

 Color/visual TO DO:
o Align color palate with warmth of the desert / desert scenery – without being to “Western”
o Incorporate sky blues, and tones found in flowers
o Feature vegetal, floral, or similar imagery (preferably that of the actual retreat location and surrounding
area)

 Color /visual DO NOT DO:
o Overly bright, pop color tones
o Sharp, bright tones
o Overtly “stock” photos – note: you can use these, but try to steer clear of obviously fake photos.

Industry/Entity Type

Healthcare

Requirements
Must have
• Must list services offers
Must use real photos of retreat and/or cooking shots
Must use at least one photo of the pool

Must have email, website and phone number

I do not want the mail ready set up. These postcards are for event handouts only.

I would like different information on each side of the postcard. Possibly, services on one side and photos/visuals on the other side with contact information on either or both sides. I attached an example of previous printed materials as well as my website to get a feel for my business.

Additionally, once this project is done, I would like to work with the designer for other elements? I'm looking for a matching business card and tri-fold brochure.

```html
<!DOCTYPE html>
<html lang="en">
<head>
<meta charset="utf-8">
<title>Stay · Play · Learn · Grow</title>
<link rel="stylesheet" href="https://fonts.googleapis.com/css2?family=Archivo+Black&family=Questrial&display=swap">
<style>
  :root {
    --paper: #ffffff;
    --ink: #2a2420;
    --stay: #c8c7ad;
    --play: #a4637a;
    --learn: #b45a3e;
    --grow: #8fa566;
    --sky: #7fa6bd;
    --rule: #e4d8c8;
    --label-text: #ffffff;
  }
  * { box-sizing: border-box; margin: 0; padding: 0; }
  html, body {
    width: 1200px;
    height: 930px;
    overflow: hidden;
    background: var(--paper);
  }
  .card {
    position: relative;
    width: 1200px;
    height: 930px;
    background: var(--paper);
  }
  .services {
    display: grid;
    grid-template-columns: 270px 293px 313px 314px;
    column-gap: 3.33px;
  }
  .service { display: flex; flex-direction: column; }
  .service__visual { height: 435px; }
  .service--stay .service__visual {
    background: linear-gradient(160deg, #4a3a26 0%, #8a6a44 35%, #e9dcc6 60%, #cdbda4 100%);
  }
  .service--play .service__visual {
    background: linear-gradient(180deg, #d8642a 0%, #b55a2c 30%, #7e3b46 60%, #4d6d3a 85%, #6f5638 100%);
  }
  .service--learn .service__visual {
    background: linear-gradient(135deg, #e6ecf0 0%, #f4f6f8 45%, #c9d3db 75%, #6d7a87 100%);
  }
  .service--grow .service__visual {
    background: linear-gradient(180deg, #e8cfc2 0%, #d9b3a2 50%, #ecd8cc 100%);
  }
  .service__label {
    height: 60px;
    margin-top: 3px;
    display: flex;
    align-items: center;
    justify-content: center;
    font-family: "Archivo Black", "Arial Black", sans-serif;
    font-size: 36px;
    font-weight: 400;
    letter-spacing: 0.5px;
    color: var(--label-text);
    text-shadow: 2px 2px 3px rgba(0,0,0,0.4);
  }
  .service--stay .service__label { background: var(--stay); }
  .service--play .service__label { background: var(--play); }
  .service--learn .service__label { background: var(--learn); }
  .service--grow .service__label { background: var(--grow); }
  .service__copy {
    padding-top: 28px;
    font-family: "Questrial", "Century Gothic", sans-serif;
    font-size: 17px;
    line-height: 30px;
    color: var(--ink);
  }
  .service__copy p + p { margin-top: 20px; }
  .service--stay .service__copy { padding-left: 51px; }
  .service--play .service__copy { padding-left: 23px; }
  .service--play .service__copy p + p { margin-top: 18px; }
  .service--learn .service__copy { padding-left: 33px; }
  .service--grow .service__copy { padding-left: 35px; }
  .service--learn .service__copy p + p,
  .service--grow .service__copy p + p { margin-top: 30px; }

  .contact {
    position: absolute;
    left: 0;
    right: 0;
    bottom: 0;
    height: 62px;
    border-top: 2px solid var(--rule);
    display: flex;
    align-items: center;
    justify-content: center;
    gap: 44px;
    font-family: "Questrial", "Century Gothic", sans-serif;
    font-size: 17px;
    color: var(--ink);
  }
  .contact__item { display: flex; align-items: center; gap: 10px; }
  .contact__icon { width: 18px; height: 18px; flex: none; }
</style>
</head>
<body>
<main class="card">
  <div class="services">
    <section class="service service--stay">
      <div class="service__visual" role="img" aria-label="Photo of a cosy retreat bedroom with cream bedding and peach and aqua pillows"></div>
      <h2 class="service__label">STAY</h2>
      <div class="service__copy">
        <p>An overnight retreat<br>focused on learning and<br>implementing the steps to<br>healthy eating and overall<br>wellness in a small group.</p>
        <p>Bed and Breakfast stays<br>catering to gluten-free<br>and whole food diets.</p>
      </div>
    </section>

    <section class="service service--play">
      <div class="service__visual" role="img" aria-label="Photo of farmers market crates with carrots, beets and cucumbers"></div>
      <h2 class="service__label">PLAY</h2>
      <div class="service__copy">
        <p>Grocery store or Farmer’s<br>Market tours with full explanations<br>of labels, ingredients, and how<br>to shop.</p>
        <p>Cooking classes at the retreat or<br>in your home or at the location of<br>your choice.</p>
        <p>Hikes and outdoor activities led<br>by Maren and guests.</p>
      </div>
    </section>

    <section class="service service--learn">
      <div class="service__visual" role="img" aria-label="Photo of a nutrition table of foods beside a calculator"></div>
      <h2 class="service__label">LEARN</h2>
      <div class="service__copy">
        <p>Indiviualized nutrition counseling<br>forindividuals, couples, families,<br>and groups.</p>
        <p>Community events, speaking<br>engagements, and classes at the<br>location of your choosing.</p>
      </div>
    </section>

    <section class="service service--grow">
      <div class="service__visual" role="img" aria-label="Photo of hands forming a heart shape over a belly"></div>
      <h2 class="service__label">GROW</h2>
      <div class="service__copy">
        <p>Intensive individualized<br>programming focused on<br>overcoming health challenges<br>and chronic illnesses.</p>
        <p>Customized on-site stays at<br>the Retreat to begin the<br>pathway to healing.</p>
      </div>
    </section>
  </div>

  <footer class="contact">
    <span class="contact__item">
      <svg class="contact__icon" viewBox="0 0 24 24" aria-hidden="true"><circle cx="12" cy="12" r="10" fill="none" stroke="var(--sky)" stroke-width="2"/><path d="M2 12h20M12 2c3 3 3 17 0 20M12 2c-3 3-3 17 0 20" fill="none" stroke="var(--sky)" stroke-width="1.6"/></svg>
      www.hollowpinekitchen.net
    </span>
    <span class="contact__item">
      <svg class="contact__icon" viewBox="0 0 24 24" aria-hidden="true"><rect x="2" y="5" width="20" height="14" rx="2" fill="none" stroke="var(--sky)" stroke-width="2"/><path d="M3 6l9 7 9-7" fill="none" stroke="var(--sky)" stroke-width="2"/></svg>
      hello@hollowpinekitchen.net
    </span>
    <span class="contact__item">
      <svg class="contact__icon" viewBox="0 0 24 24" aria-hidden="true"><path d="M6.5 3h3l1.5 5-2 1.5a11 11 0 0 0 5.5 5.5l1.5-2 5 1.5v3a2 2 0 0 1-2 2A17 17 0 0 1 4.5 5a2 2 0 0 1 2-2z" fill="none" stroke="var(--sky)" stroke-width="2" stroke-linejoin="round"/></svg>
      (555) 014-2738
    </span>
  </footer>
</main>
</body>
</html>
```